recipe card template

desgin an AI file that is a template for a recipe card. We are an Organic beef farm wanting to give customers recipe cards for our different beef cuts. Looking at doing something black & white that says premium product from a family farm.

Target Market(s)

people who want quality produce

Industry/Entity Type

Farm

Font styles to use
Serif
Sans Serif

Colors

Designer to choose colors to be used in the design.

Requirements
Must have
• Instruction section - ingredients section - "bramblecote produce family farm" title
Nice to have
• images etc that refer to beef and eggs

```html
<!DOCTYPE html>
<html lang="en">
<head>
<meta charset="utf-8">
<title>Chuck Recipe Card</title>
<link href="https://fonts.googleapis.com/css2?family=Lato:wght@400;700&family=Oswald:wght@300&family=Pacifico&display=swap" rel="stylesheet">
<style>
  :root {
    --page: #d9d9d9;
    --card: #f3f3f3;
    --photo-dark: #1f1c1a;
    --photo-warm: #6b4a35;
    --accent: #86ad73;
    --accent-dark: #5e8a4d;
    --rule: #8fb27c;
    --text-light: #f2f2f2;
    --text-body: #6a6a6a;
    --icon: #8a8a8a;
    --cow: #a9a9a9;
  }
  * { margin: 0; padding: 0; box-sizing: border-box; }
  html, body { width: 1200px; height: 686px; overflow: hidden; }
  body { background: var(--page); position: relative; font-family: 'Lato', sans-serif; }

  .recipe-card {
    position: absolute; left: 130px; top: 21px;
    width: 940px; height: 644px;
    background: var(--card);
    display: flex;
    box-shadow: 0 4px 14px rgba(0,0,0,.18);
  }

  .photo-column {
    position: relative; width: 315px; height: 100%; overflow: hidden;
    background: linear-gradient(160deg, #2b2521 0%, var(--photo-warm) 45%, #3a2a20 70%, var(--photo-dark) 100%);
  }
  .photo-column .food-photo { position: absolute; inset: 0; }
  .farm-mark {
    position: absolute; left: 0; right: 0; top: 400px;
    text-align: center; color: var(--text-light);
    font-family: 'Lato', sans-serif; font-weight: 400; font-size: 15px; letter-spacing: 1px;
  }
  .farm-block {
    position: absolute; left: 24px; right: 24px; top: 470px;
    color: var(--text-light); text-align: center;
  }
  .farm-block .rule { height: 2px; background: var(--rule); }
  .farm-title {
    font-family: 'Lato', sans-serif; font-weight: 400;
    font-size: 21px; line-height: 1.3; letter-spacing: .5px; text-transform: uppercase;
    white-space: nowrap;
    padding: 8px 0 6px;
  }
  .recipe-meta { font-size: 14px; line-height: 1.5; margin-top: 10px; text-transform: uppercase; }
  .recipe-meta span { text-transform: none; }

  .recipe-panel { position: relative; flex: 1; }
  .title-band {
    position: absolute; left: 0; right: 0; top: 20px; height: 62px;
    background: var(--accent);
    display: flex; align-items: center; padding-left: 16px;
  }
  .recipe-title { font-family: 'Pacifico', cursive; font-weight: 400; font-size: 38px; color: #fff; line-height: 1; }

  .section { position: absolute; left: 30px; }
  .section-label {
    font-family: 'Oswald', sans-serif; font-weight: 300; font-size: 27px;
    color: var(--accent-dark); text-transform: uppercase; letter-spacing: .5px;
  }
  .section-body { font-size: 18px; color: var(--text-body); margin-top: 2px; }
  .ingredients { top: 96px; }
  .instructions { top: 224px; }

  .cut-diagram { position: absolute; left: 20px; top: 400px; width: 318px; height: 225px; }

  .social { position: absolute; left: 386px; top: 560px; color: var(--text-body); font-size: 17px; }
  .social-icons { display: flex; gap: 15px; margin-top: 8px; }
  .social-icons i { width: 20px; height: 20px; background: var(--icon); border-radius: 3px; display: block; }
</style>
</head>
<body>
  <article class="recipe-card">
    <aside class="photo-column">
      <div class="food-photo" role="img" aria-label="Photograph of a grilled steak with tomatoes, zucchini and herbs on a dark board"></div>
      <div class="farm-mark">Hollin Ridge Farms</div>
      <div class="farm-block">
        <div class="rule"></div>
        <h1 class="farm-title">Bramblecote Produce<br>Family Farm</h1>
        <div class="rule"></div>
        <p class="recipe-meta">Total time: <span>45 minutes</span><br>Servings: 2</p>
      </div>
    </aside>

    <section class="recipe-panel">
      <header class="title-band"><h2 class="recipe-title">Chuck Recipe</h2></header>

      <div class="section ingredients">
        <h3 class="section-label">Ingredients:</h3>
        <p class="section-body">Lorem ipasum</p>
      </div>

      <div class="section instructions">
        <h3 class="section-label">Instruction:</h3>
        <p class="section-body">Lorem ipasum</p>
      </div>

      <svg class="cut-diagram" viewBox="0 0 318 225" role="img" aria-label="Beef cuts diagram of a cow with the chuck section highlighted">
        <rect x="0" y="0" width="318" height="225" rx="24" fill="var(--cow)" opacity=".55"/>
        <rect x="190" y="30" width="70" height="75" rx="10" fill="var(--accent)"/>
      </svg>

      <div class="social">
        <p>find us on:</p>
        <div class="social-icons"><i></i><i></i><i></i><i></i><i></i></div>
      </div>
    </section>
  </article>
</body>
</html>
```